Dietitian clinic needs a business card design

We need a business card design for a new dietitian group based in Singapore called "Lantern and Tide". We provide expert, personalised nutrition care to support a wide range of health needs, from chronic conditions to mindful eating. Our team also offers consulting, speaking, and tailored solutions for healthcare providers, organisations, and food services.

Target Market(s)

Adults

Industry/Entity Type

Healthcare

Contact Information for Business Card

Name, position, contact number, email, website address, our logo

Requirements
Nice to have
• Clean, professional but welcoming look

```html
<!DOCTYPE html>
<html lang="en">
<head>
<meta charset="UTF-8">
<title>Lantern and Tide — Business Card</title>
<link rel="stylesheet" href="https://fonts.googleapis.com/css2?family=Playfair+Display:wght@700&family=Tinos:wght@400;700&display=swap">
<style>
  :root {
    --stage: #2c2e31;
    --teal: #1f566b;
    --paper: #ffffff;
    --ink-soft: #5b5f63;
    --rule: #b9bcbf;
  }
  * { box-sizing: border-box; margin: 0; padding: 0; }
  html, body {
    width: 1200px;
    height: 985px;
    overflow: hidden;
    background: var(--stage);
  }
  .canvas {
    width: 1200px;
    height: 985px;
    display: flex;
    align-items: center;
    justify-content: center;
    gap: 50px;
  }
  .card {
    width: 525px;
    height: 300px;
    border-radius: 24px;
    position: relative;
    overflow: hidden;
    box-shadow: 0 18px 40px rgba(0,0,0,0.35);
  }

  /* Front */
  .card-front {
    background: var(--paper);
    display: flex;
    align-items: center;
  }
  .front-brand {
    width: 236px;
    padding-left: 34px;
    display: flex;
    align-items: center;
    gap: 10px;
  }
  .brand-dot {
    width: 12px;
    height: 12px;
    border-radius: 50%;
    background: var(--teal);
    flex: none;
  }
  .brand-name {
    font-family: "Tinos", "Times New Roman", serif;
    font-weight: 400;
    color: var(--teal);
    font-size: 22px;
    line-height: 1.2;
    white-space: nowrap;
  }
  .front-divider {
    width: 1px;
    height: 150px;
    background: var(--rule);
    margin: 0 28px 0 0;
    flex: none;
  }
  .front-details {
    font-family: "Tinos", "Times New Roman", serif;
    color: var(--ink-soft);
  }
  .person-name {
    font-family: "Playfair Display", Georgia, serif;
    font-weight: 700;
    color: var(--teal);
    font-size: 22px;
    line-height: 1;
  }
  .person-role {
    font-size: 13px;
    margin-top: 3px;
  }
  .address {
    font-size: 13px;
    line-height: 1.3;
    margin-top: 14px;
  }
  .contact-list {
    list-style: none;
    margin-top: 12px;
    font-size: 13px;
    line-height: 1;
  }
  .contact-list li {
    display: flex;
    align-items: center;
    gap: 7px;
    margin-bottom: 5px;
  }
  .contact-icon {
    width: 13px;
    height: 13px;
    flex: none;
  }

  /* Back */
  .card-back {
    background: var(--teal);
    display: flex;
    align-items: center;
    justify-content: center;
  }
  .back-name {
    font-family: "Tinos", "Times New Roman", serif;
    font-weight: 400;
    color: var(--paper);
    font-size: 44px;
    line-height: 1.2;
    white-space: nowrap;
  }
</style>
</head>
<body>
<main class="canvas">

  <section class="card card-front" aria-label="Business card front">
    <div class="front-brand">
      <span class="brand-dot"></span>
      <div class="brand-name">Lantern and Tide</div>
    </div>
    <div class="front-divider"></div>
    <div class="front-details">
      <h1 class="person-name">Mara Ellison</h1>
      <p class="person-role">Managing Director</p>
      <p class="address">PO Box 418 Harbour Row<br>Singapore</p>
      <ul class="contact-list">
        <li>
          <svg class="contact-icon" viewBox="0 0 16 16" aria-hidden="true">
            <circle cx="8" cy="8" r="8" fill="#1f566b"/>
            <path d="M5.5 4.2l1.3-.3.8 2-1 .7c.5 1.1 1.3 1.9 2.4 2.4l.7-1 2 .8-.3 1.3c-3.4.2-6.1-2.5-5.9-5.9z" fill="#fff"/>
          </svg>
          234-610-4452
        </li>
        <li>
          <svg class="contact-icon" viewBox="0 0 16 16" aria-hidden="true">
            <circle cx="8" cy="8" r="8" fill="#1f566b"/>
            <rect x="4" y="5.2" width="8" height="5.6" fill="none" stroke="#fff" stroke-width="1"/>
            <path d="M4 5.2l4 3 4-3" fill="none" stroke="#fff" stroke-width="1"/>
          </svg>
          hello@lanternandtide.com
        </li>
        <li>
          <svg class="contact-icon" viewBox="0 0 16 16" aria-hidden="true">
            <circle cx="8" cy="8" r="8" fill="#1f566b"/>
            <circle cx="8" cy="8" r="4" fill="none" stroke="#fff" stroke-width="1"/>
            <path d="M4 8h8M8 4c-1.6 2.4-1.6 5.6 0 8M8 4c1.6 2.4 1.6 5.6 0 8" fill="none" stroke="#fff" stroke-width="0.9"/>
          </svg>
          www.lanternandtide.com
        </li>
      </ul>
    </div>
  </section>

  <section class="card card-back" aria-label="Business card back">
    <div class="back-name">Lantern and Tide</div>
  </section>

</main>
</body>
</html>
```